WEBSITE DESIGN - www.brindolux.com

We need a professional and modern looking website for our business. The current website was only made tentatively and can be viewed (we expect a website MUCH better than this). It needs to be simple and non-cluttered yet look modern and sophisticated. It needs to be very easy to navigate as our tarket market is people over the age of 45. Our logo is attached below and this should be incorporated plus the colours/theme should match this. We don't mind purchasing images online if your design includes these and we like it.

Any other specific questions please enquire as we want to hear them.

Target Market(s)

over 45 age english speaking westerners

Industry/Entity Type

Business

Number of Pages Required

1 page

Requirements
Must have
• -our logo (attached).
• -page tabs as those described (tabs.. but not necessarily each of these pages completed as well although this would be nice).
• -social media logos
• Pages should include: homepage, services, pricing, about us, contact us. There should also be a payments page designed which would link with the other pages but there would be no tab for this.

```html
<!DOCTYPE html>
<html lang="en">
<head>
<meta charset="utf-8">
<title>Brindolux – Computer Solutions</title>
<link rel="stylesheet" href="https://fonts.googleapis.com/css2?family=Open+Sans:wght@400;600;700&display=swap">
<style>
:root{
  --orange:#e9a100;
  --orange-dark:#c98a00;
  --ink:#2b2b2b;
  --muted:#8a8a8a;
  --line:#dcdcdc;
  --dark:#1c1c1c;
  --darker:#141414;
  --paper:#ffffff;
  --soft:#f3f3f3;
  --purple:#7d2a8c;
  --green:#16603f;
  --magenta:#9a1a67;
  --blue:#2b82bd;
  --teal:#12707a;
}
*{box-sizing:border-box;margin:0;padding:0}
html,body{width:1200px;height:3673px;overflow:hidden}
body{font-family:"Open Sans",Arial,sans-serif;color:var(--ink);background:var(--paper);position:relative}
section,header,footer{position:absolute;left:0;width:1200px}

/* hero */
.hero{top:0;height:588px}
.hero-photo{position:absolute;inset:0;background:radial-gradient(ellipse at 62% 45%,#8fe0f5 0%,#2f8fb7 22%,#123f5c 55%,#0a1a28 100%)}
.brand{position:absolute;left:61px;top:0;width:180px;height:147px;background:var(--paper);display:flex;align-items:center;justify-content:center;gap:10px;z-index:2}
.brand-dot{width:22px;height:22px;border-radius:50%;background:var(--orange)}
.brand-name{font-size:24px;font-weight:700;color:var(--ink)}
.nav{position:absolute;left:240px;right:0;top:44px;height:59px;background:rgba(20,20,20,.82);display:flex;padding-left:176px}
.nav a{color:#fff;text-decoration:none;font-size:14px;font-weight:700;display:flex;align-items:center;justify-content:center;width:148px}
.nav a.active{background:var(--orange);width:123px}

/* about */
.about{top:588px;height:568px;text-align:center}
.section-title{font-size:22px;font-weight:700;color:#333;letter-spacing:.5px}
.section-title span{color:var(--orange)}
.section-title::after{content:"";display:block;width:120px;height:2px;background:var(--orange);margin:10px auto 0}
.about .section-title{margin-top:42px}
.about h3{font-size:20px;font-weight:600;color:#222;margin-top:6px}
.about .lead{font-size:15px;color:var(--muted);margin-top:8px}
.features{position:absolute;top:180px;left:50px;width:1100px;display:flex;justify-content:space-between}
.feature{width:270px}
.icon-circle{width:76px;height:76px;border-radius:50%;background:var(--orange);margin:0 auto;display:flex;align-items:center;justify-content:center}
.feature h4{font-size:14px;font-weight:700;color:var(--orange);margin-top:14px;text-transform:uppercase}
.feature p{font-size:13.5px;line-height:21px;color:#666;margin-top:8px;height:63px;overflow:hidden}
.feature .more{font-size:13px;color:#444;margin-top:6px}
.skills{position:absolute;top:440px;left:59px;width:1092px;display:grid;grid-template-columns:345px 343px 345px;column-gap:27px;row-gap:26px;text-align:left}
.skill-head{display:flex;justify-content:space-between;font-size:13px;font-weight:600}
.skill-head span:last-child{color:#555;font-weight:400}
.track{height:7px;background:#e3e3e3;margin-top:5px;position:relative;border-radius:4px}
.fill{position:absolute;left:0;top:0;bottom:0;border-radius:4px}
.fill::after{content:"";position:absolute;right:-4px;top:-3px;width:13px;height:13px;border-radius:50%;background:inherit}

/* stats */
.stats{top:1156px;height:294px}
.stats-photo{position:absolute;inset:0;background:linear-gradient(180deg,#2a2a2e 0%,#16161a 100%)}
.stats-row{position:absolute;inset:0;display:flex;justify-content:space-between;padding:56px 40px 0 55px}
.stat{width:180px;text-align:center;color:#fff}
.stat .icon-circle{width:84px;height:84px;border:4px solid rgba(255,255,255,.85)}
.stat strong{display:block;font-size:40px;font-weight:700;margin-top:10px}
.stat span{display:block;font-size:16px;margin-top:2px;line-height:20px}

/* services */
.services{top:1450px;height:333px;text-align:center}
.services .section-title{margin-top:28px}
.service-cards{position:absolute;top:93px;left:59px;width:1094px;height:196px}
.service{position:absolute;top:0;width:253px;height:196px;background:var(--orange);color:#fff;padding:76px 20px 0}
.service .icon-circle{position:absolute;top:-37px;left:84px;width:84px;height:84px;border:4px solid #fff}
.service h4{font-size:14px;font-weight:700}
.service p{font-size:13.5px;line-height:19px;margin-top:10px}

/* testimonials */
.clients{top:1783px;height:397px;text-align:center;color:#fff}
.clients-photo{position:absolute;inset:0;background:linear-gradient(180deg,#262626 0%,#1a1a1a 100%)}
.clients .section-title{position:relative;margin-top:34px;color:#fff}
.clients .section-title::after{display:none}
.quote-mark{position:absolute;top:112px;font-size:60px;font-weight:700;color:#ddd;line-height:1}
.avatar{position:absolute;left:539px;top:108px;width:122px;height:122px;border-radius:50%;border:5px solid #fff;background:radial-gradient(circle at 50% 40%,#f3d7b8,#c9a17c 70%)}
.arrow-btn{position:absolute;top:2000px;width:30px;height:30px;border:1px solid #777;display:flex;align-items:center;justify-content:center}
.client-name{position:absolute;top:243px;left:0;right:0;font-size:16px;font-weight:600;color:var(--orange)}
.client-text{position:absolute;top:290px;left:0;right:0;font-size:15px;line-height:27px;color:#bbb}

/* plans */
.plans{top:2180px;height:710px;background:var(--soft);text-align:center}
.plans .section-title{margin-top:42px}
.plan{position:absolute;background:#fff;box-shadow:0 0 6px rgba(0,0,0,.08);padding:0 22px}
.plan-tag{width:142px;margin:0 auto;background:var(--orange);color:#fff;padding:10px 0 8px;font-size:15px;font-weight:700;line-height:18px}
.plan-tag small{display:block;font-size:11px;font-weight:600}
.plan-price{font-size:22px;font-weight:600;color:#555;margin:22px 0 12px;word-spacing:6px}
.plan-note{font-size:15px;line-height:21px;color:#222;margin-bottom:10px}
.plan ul{list-style:none;border-top:2px dotted #bbb}
.plan li{font-size:14.5px;color:#444;padding:13px 0 12px;border-bottom:2px dotted #bbb}
.plan li:last-child{border-bottom:none}
.agree{display:flex;align-items:center;justify-content:center;gap:9px;font-size:15px;margin-top:12px}
.agree i{width:17px;height:17px;border:1px solid #555;border-radius:2px;background:#fff}
.plan-btn{display:inline-block;margin-top:18px;padding:8px 18px;font-size:15px;border:2px solid #888;color:#555;font-weight:600}
.plan-btn.primary{background:var(--orange);border-color:var(--orange);color:#fff;font-weight:700}

/* payments */
.payments{top:2890px;height:201px;background:#fff}
.pay-card{position:absolute;top:37px;width:134px;height:110px;border:1px solid #e2e2e2;display:flex;align-items:center;justify-content:center;gap:7px}
.pay-card b{font-size:17px;font-weight:700;color:#2b2b2b}
.pay-card i{width:14px;height:14px;border-radius:50%;background:var(--orange);display:block}
.pay-arrow{position:absolute;top:76px;width:34px;height:34px;border-radius:50%;border:1px solid #bbb;display:flex;align-items:center;justify-content:center}

/* contact */
.contact{top:3091px;height:448px;background:var(--darker);text-align:center;color:#ccc}
.contact .section-title{margin-top:44px;color:#fff;font-size:20px}
.contact .section-title::after{display:none}
.info{position:absolute;top:92px;left:59px;width:1092px;display:flex;justify-content:space-between;text-align:left}
.info-item{display:flex;gap:22px;width:350px}
.ring{flex:none;width:62px;height:62px;border-radius:50%;border:2px solid var(--orange);display:flex;align-items:center;justify-content:center}
.info-item p{font-size:13.5px;line-height:22px;color:#ccc}
.form{position:absolute;top:227px;left:59px;width:1092px}
.inputs{display:flex;justify-content:space-between}
.field{width:345px;height:46px;border:1px solid #444;font-size:14px;color:#999;padding:12px 16px;text-align:left}
.msg-row{display:flex;justify-content:space-between;margin-top:29px}
.field.msg{width:943px;height:100px}
.send{width:121px;height:100px;background:var(--orange);color:#fff;font-size:26px;font-weight:700;display:flex;align-items:center;justify-content:center}

/* footer */
.footer{top:3539px;height:134px;background:#fff}
.disclaimer{text-align:center;font-size:13px;color:#555;line-height:24px;margin-top:36px}
.footer-bar{position:absolute;left:59px;right:49px;top:90px;border-top:1px solid #ddd;padding-top:10px;display:flex;justify-content:space-between;align-items:center}
.copy{font-size:13px;color:#555}
.copy span{color:var(--orange)}
.socials{display:flex;gap:10px}
.social{display:flex;align-items:center;gap:4px;font-size:11px;color:#666}
.social i{width:12px;height:12px;border-radius:50%;background:var(--orange);display:block}
</style>
</head>
<body>

<header class="hero">
  <div class="hero-photo" role="img" aria-label="Photo of a young man in glasses holding a laptop in front of glowing blue technology icons"></div>
  <div class="brand"><span class="brand-dot"></span><span class="brand-name">Brindolux</span></div>
  <nav class="nav">
    <a class="active" href="#">HOME</a>
    <a href="#">ABOUT US</a>
    <a href="#">SERVICES</a>
    <a href="#">PRICING</a>
    <a href="#">CONTACT US</a>
  </nav>
</header>

<section class="about">
  <h2 class="section-title">ABOUT <span>BRINDOLUX</span></h2>
  <h3>Why We Are The Best</h3>
  <p class="lead">The one stop comprehensive diagnostic &amp; repair station for your computer and connected devices. We'll fix anything!</p>
  <div class="features">
    <div class="feature">
      <div class="icon-circle"><svg width="38" height="38" viewBox="0 0 24 24" fill="none" stroke="#fff" stroke-width="1.8"><rect x="3" y="4" width="18" height="12" rx="1"/><path d="M8 20h8M12 16v4M7 12l3-3 2 2 4-4"/></svg></div>
      <h4>Diagnosis &amp; Repair</h4>
      <p>The one stop comprehensive diagnostic &amp; repair station for your computer and connected devices. We'll fix anything!</p>
      <div class="more">More ▾</div>
    </div>
    <div class="feature">
      <div class="icon-circle"><svg width="38" height="38" viewBox="0 0 24 24" fill="none" stroke="#fff" stroke-width="1.8"><circle cx="12" cy="12" r="3"/><path d="M12 3v3M12 18v3M3 12h3M18 12h3M5.6 5.6l2.1 2.1M16.3 16.3l2.1 2.1M5.6 18.4l2.1-2.1M16.3 7.7l2.1-2.1"/></svg></div>
      <h4>Setup &amp; Install</h4>
      <p>Confused and frustrated with device setup &amp; installation? Leave it to the experts, which means all</p>
      <div class="more">More ▾</div>
    </div>
    <div class="feature">
      <div class="icon-circle"><svg width="38" height="38" viewBox="0 0 24 24" fill="none" stroke="#fff" stroke-width="1.8"><rect x="3" y="4" width="18" height="13" rx="1"/><path d="M9 21h6M6 14l4-4 3 3 5-5"/></svg></div>
      <h4>Optimization</h4>
      <p>You won't believe it's the same old computer. Your system will work like it did on the day you bought it</p>
      <div class="more">More ▾</div>
    </div>
    <div class="feature">
      <div class="icon-circle"><svg width="38" height="38" viewBox="0 0 24 24" fill="none" stroke="#fff" stroke-width="1.8"><path d="M5 13v-2a7 7 0 0 1 14 0v2"/><rect x="3" y="12" width="4" height="6" rx="1"/><rect x="17" y="12" width="4" height="6" rx="1"/><path d="M19 18c0 2-2 3-5 3"/></svg></div>
      <h4>Support</h4>
      <p>We develop the website, we analyse, strategize and assess our client's specific need,requirement,preference</p>
      <div class="more">More ▾</div>
    </div>
  </div>
  <div class="skills">
    <div class="skill"><div class="skill-head"><span style="color:var(--orange)">AWESOMENESS</span><span>95%</span></div><div class="track"><div class="fill" style="width:95%;background:var(--orange)"></div></div></div>
    <div class="skill"><div class="skill-head"><span style="color:var(--purple)">SUPPORT</span><span>100%</span></div><div class="track"><div class="fill" style="width:98%;background:var(--purple)"></div></div></div>
    <div class="skill"><div class="skill-head"><span style="color:var(--green)">FLEXIBILITY</span><span>98%</span></div><div class="track"><div class="fill" style="width:98%;background:var(--green)"></div></div></div>
    <div class="skill"><div class="skill-head"><span style="color:var(--magenta)">SOFTWARE INSTALLATION</span><span>97%</span></div><div class="track"><div class="fill" style="width:97%;background:var(--magenta)"></div></div></div>
    <div class="skill"><div class="skill-head"><span style="color:var(--blue)">VIRUS REMOVAL</span><span>93%</span></div><div class="track"><div class="fill" style="width:93%;background:var(--blue)"></div></div></div>
    <div class="skill"><div class="skill-head"><span style="color:var(--teal)">SYSTEM SETUP</span><span>98%</span></div><div class="track"><div class="fill" style="width:98%;background:var(--teal)"></div></div></div>
  </div>
</section>

<section class="stats">
  <div class="stats-photo" role="img" aria-label="Darkened photo of a smiling business team"></div>
  <div class="stats-row">
    <div class="stat"><div class="icon-circle"><svg width="36" height="36" viewBox="0 0 24 24" fill="none" stroke="#fff" stroke-width="1.8"><rect x="5" y="5" width="14" height="10" rx="1"/><path d="M2 18h20"/></svg></div><strong>986</strong><span>Laptops</span></div>
    <div class="stat"><div class="icon-circle"><svg width="36" height="36" viewBox="0 0 24 24" fill="none" stroke="#fff" stroke-width="1.8"><rect x="3" y="13" width="18" height="6" rx="1"/><path d="M7 13V6M17 13V6M9 8a4 4 0 0 1 6 0"/></svg></div><strong>256</strong><span>Routers</span></div>
    <div class="stat"><div class="icon-circle"><svg width="36" height="36" viewBox="0 0 24 24" fill="none" stroke="#fff" stroke-width="1.8"><rect x="7" y="3" width="10" height="18" rx="2"/><path d="M11 18h2"/></svg></div><strong>867</strong><span>Smart Phones</span></div>
    <div class="stat"><div class="icon-circle"><svg width="36" height="36" viewBox="0 0 24 24" fill="none" stroke="#fff" stroke-width="1.8"><rect x="3" y="4" width="18" height="12" rx="1"/><path d="M9 20h6M12 16v4"/></svg></div><strong>1904</strong><span>Desktops</span></div>
    <div class="stat"><div class="icon-circle"><svg width="36" height="36" viewBox="0 0 24 24" fill="none" stroke="#fff" stroke-width="1.8"><rect x="4" y="3" width="16" height="18" rx="2"/><circle cx="12" cy="18" r=".8"/></svg></div><strong>511</strong><span>Tablets</span></div>
    <div class="stat"><div class="icon-circle"><svg width="36" height="36" viewBox="0 0 24 24" fill="none" stroke="#fff" stroke-width="1.8"><rect x="3" y="4" width="18" height="13" rx="1"/><path d="M12 7v6M9 10l3 3 3-3M9 21h6"/></svg></div><strong>2456</strong><span>Software<br>Installation</span></div>
  </div>
</section>

<section class="services">
  <h2 class="section-title">BEST <span>SERVICES</span></h2>
  <div class="service-cards">
    <div class="service" style="left:0"><div class="icon-circle"><svg width="36" height="36" viewBox="0 0 24 24" fill="none" stroke="#fff" stroke-width="1.8"><rect x="3" y="4" width="15" height="11" rx="1"/><path d="M14 19h7v-6"/></svg></div><h4>TECH SUPPORT</h4><p>We make technology easier for you with instant support.</p></div>
    <div class="service" style="left:281px"><div class="icon-circle"><svg width="36" height="36" viewBox="0 0 24 24" fill="none" stroke="#fff" stroke-width="1.8"><path d="M7 17a4 4 0 0 1 0-8 6 6 0 0 1 11 1 3.5 3.5 0 0 1-1 7"/><path d="M12 11v9M9 17l3 3 3-3"/></svg></div><h4>DOWNLOADS</h4><p>The best apps to optimize &amp; secure your digital devices.</p></div>
    <div class="service" style="left:563px"><div class="icon-circle"><svg width="36" height="36" viewBox="0 0 24 24" fill="none" stroke="#fff" stroke-width="1.8"><rect x="3" y="4" width="18" height="12" rx="1"/><path d="M9 20h6M12 16v4M10 8l4 4"/></svg></div><h4>WEB DESIGN</h4><p>We understand that every business owner has his own way of showcasing products</p></div>
    <div class="service" style="left:842px"><div class="icon-circle"><svg width="36" height="36" viewBox="0 0 24 24" fill="none" stroke="#fff" stroke-width="1.8"><rect x="4" y="4" width="16" height="16" rx="1"/><path d="M8 9h8M8 13h8M8 17h5"/></svg></div><h4>UNDERSTAND THE URGENCY</h4><p>We believe in careful planning for you.</p></div>
  </div>
</section>

<section class="clients">
  <div class="clients-photo" role="img" aria-label="Darkened collage of client portraits"></div>
  <h2 class="section-title">WHAT OUR <span>HAPPY CLIENTS SAY</span></h2>
  <div class="quote-mark" style="left:496px">“</div>
  <div class="quote-mark" style="left:682px">”</div>
  <div class="avatar" role="img" aria-label="Client portrait"></div>
  <div class="arrow-btn" style="top:217px;left:125px"><svg width="12" height="12" viewBox="0 0 12 12" fill="none" stroke="#999" stroke-width="1.6"><path d="M8 2L4 6l4 4"/></svg></div>
  <div class="arrow-btn" style="top:217px;left:1055px"><svg width="12" height="12" viewBox="0 0 12 12" fill="none" stroke="#999" stroke-width="1.6"><path d="M4 2l4 4-4 4"/></svg></div>
  <div class="client-name">Marla Tenby</div>
  <p class="client-text">Thank for such a Support. Quality Support. I'm extremely impressed. It has been one of the best experiences.<br>So pleased with u Brindolux.You r d best.</p>
</section>

<section class="plans">
  <h2 class="section-title">OUR <span>PLANS</span></h2>
  <div class="plan" style="left:59px;top:154px;width:345px;height:446px">
    <div class="plan-tag">QUICK FIX<small>1 Month</small></div>
    <div class="plan-price">NZD 95 USD 60* GBP 40*</div>
    <ul><li>1 Month Tech Support</li><li>For 1 Computer</li><li>24X7 Availability</li></ul>
    <div class="agree"><i></i>I agree to the Terms and Conditions</div>
    <div class="plan-btn">GET START NOW</div>
  </div>
  <div class="plan" style="left:431px;top:112px;width:348px;height:524px">
    <div class="plan-tag">ADVANCE<small>1 Year</small></div>
    <div class="plan-price">NZD 250 USD 160* GBP 105*</div>
    <p class="plan-note">*The price advertised might not be the price charged to the credit card account due to exchange rate fluctuations.</p>
    <ul><li>1 Year Tech Support</li><li>Upto 3 Computers &amp; Printers</li><li>Connected Devices with Router</li></ul>
    <div class="agree"><i></i>I agree to the Terms and Conditions</div>
    <div class="plan-btn primary">GET START NOW</div>
  </div>
  <div class="plan" style="left:806px;top:154px;width:345px;height:446px">
    <div class="plan-tag">STARTER<small>6 Month</small></div>
    <div class="plan-price">NZD 140 USD 90* GBP 60*</div>
    <ul><li>6 Month Tech Support</li><li>6 Month support for the same issue</li><li>24X7 Availability</li></ul>
    <div class="agree"><i></i>I agree to the Terms and Conditions</div>
    <div class="plan-btn">GET START NOW</div>
  </div>
</section>

<section class="payments">
  <div class="pay-arrow" style="left:59px"><svg width="12" height="12" viewBox="0 0 12 12" fill="none" stroke="#666" stroke-width="1.6"><path d="M8 2L4 6l4 4"/></svg></div>
  <div class="pay-card" style="left:127px"><i></i><b>Payvia</b></div>
  <div class="pay-card" style="left:290px"><i></i><b>Cardmark</b></div>
  <div class="pay-card" style="left:455px"><span style="width:60px;height:74px;border-radius:8px;background:#555;display:block" role="img" aria-label="Secure shopping badge"></span></div>
  <div class="pay-card" style="left:617px"><i></i><b>Disqua</b></div>
  <div class="pay-card" style="left:781px"><i></i><b>Payvia Swift</b></div>
  <div class="pay-card" style="left:945px"><i></i><b>Cardolo</b></div>
  <div class="pay-arrow" style="left:1107px"><svg width="12" height="12" viewBox="0 0 12 12" fill="none" stroke="#666" stroke-width="1.6"><path d="M4 2l4 4-4 4"/></svg></div>
</section>

<section class="contact">
  <h2 class="section-title">KEEP IN TOUCH <span>WITH US</span></h2>
  <div class="info">
    <div class="info-item">
      <div class="ring"><svg width="28" height="28" viewBox="0 0 24 24" fill="none" stroke="var(--orange)" stroke-width="1.8"><path d="M12 21s-6-6.3-6-11a6 6 0 0 1 12 0c0 4.7-6 11-6 11z"/><circle cx="12" cy="10" r="2.2"/></svg></div>
      <p>Kestrel Court Tower 1<br>5H/205 Kestrel Street<br>Auckland Central Auckland -1010<br>New Zeland</p>
    </div>
    <div class="info-item">
      <div class="ring"><svg width="28" height="28" viewBox="0 0 24 24" fill="none" stroke="var(--orange)" stroke-width="1.8"><path d="M5 4h4l2 5-2.5 1.5a11 11 0 0 0 5 5L15 13l5 2v4a1 1 0 0 1-1 1A16 16 0 0 1 4 5a1 1 0 0 1 1-1z"/></svg></div>
      <p>USA- +1 555 010 4821<br>UK- +44 200 000 1147<br>Australia- +61 2 5550 1936</p>
    </div>
    <div class="info-item">
      <div class="ring"><svg width="28" height="28" viewBox="0 0 24 24" fill="none" stroke="var(--orange)" stroke-width="1.8"><rect x="3" y="6" width="18" height="12" rx="1"/><path d="M3 7l9 6 9-6"/></svg></div>
      <p>For Querry - info@brindolux.com<br>For Billinh - bills@brindolux.com<br>For Suppor - support@brindolux.com</p>
    </div>
  </div>
  <div class="form">
    <div class="inputs"><div class="field">Your Name</div><div class="field">Your E-mail</div><div class="field">Your Phone</div></div>
    <div class="msg-row"><div class="field msg">Your Message</div><div class="send">SEND</div></div>
  </div>
</section>

<footer class="footer">
  <p class="disclaimer">We do not take payments through Westmark Transfer. We are not associated with Norvale, Quentix, Brightlane, Sentora, or any other Brands.<br>We are Third Party Tech Support Company.</p>
  <div class="footer-bar">
    <div class="copy">Copyright © 2016 <span>Brindolux</span>. All rights reserved.</div>
    <div class="socials">
      <span class="social"><i></i>Friendspace</span>
      <span class="social"><i></i>Chirpline</span>
      <span class="social"><i></i>Circlenet</span>
      <span class="social"><i></i>Viewtube</span>
    </div>
  </div>
</footer>

</body>
</html>
```